Simple and Approachable Cover for Pet Expo Company Page

Size: 2000 x 430; looking simply for words "Dunmore HR Consulting" and email address "DunmoreHRConsulting@brelvamail.com." This is for a cover photo for a company profile page for the Hollow Oak Expo, where I am a featured speaker on Employee Communications later this month. You can incorporate the attached photo to the left of the banner ad if you wish. The mood I wish to present is approachable, positive and simple.

Target Market(s)

small pet retail business owners

Industry/Entity Type

Pet Shop

Font styles to use
Serif
Sans Serif

Requirements
Must have
• Email address clearly defined/separated. Easy to read.
Nice to have
• I like the picture that I included; subtle pet paw background is also nice
Should not have
• No paid stock images

```html
<!DOCTYPE html>
<html lang="en">
<head>
<meta charset="utf-8">
<title>Dunmore HR Consulting – Cover Banner</title>
<link rel="stylesheet" href="https://fonts.googleapis.com/css2?family=Rubik:wght@500;700&display=swap">
<style>
  :root {
    --backdrop: #666666;
    --crimson-light: #b3001f;
    --crimson-dark: #6e0010;
    --orange: #ec870f;
    --white: #ffffff;
    --photo-sky: #7d8a5a;
    --photo-trees: #4f5b36;
    --photo-grass: #8c8a4a;
  }
  html, body {
    margin: 0;
    padding: 0;
    width: 1200px;
    height: 1000px;
    overflow: hidden;
    background: var(--backdrop);
  }
  .cover-banner {
    position: absolute;
    left: 56px;
    top: 341px;
    width: 1079px;
    height: 231px;
    overflow: hidden;
    font-family: "Rubik", Arial, sans-serif;
  }
  .banner-shapes {
    position: absolute;
    inset: 0;
    width: 100%;
    height: 100%;
  }
  .brand-name {
    position: absolute;
    left: 42px;
    top: 14px;
    margin: 0;
    color: var(--white);
    line-height: 1;
    text-transform: uppercase;
  }
  .brand-name .brand-line-top {
    display: block;
    font-weight: 500;
    font-size: 51px;
    letter-spacing: 0.5px;
  }
  .brand-name .brand-line-main {
    display: block;
    font-weight: 700;
    font-size: 66px;
    margin-top: 2px;
    letter-spacing: 0.5px;
  }
  .email-pill {
    position: absolute;
    left: 46px;
    top: 145px;
    height: 52px;
    padding: 0 14px 0 12px;
    border-radius: 0 26px 26px 0;
    background: var(--orange);
    color: var(--white);
    font-weight: 700;
    font-size: 24px;
    line-height: 52px;
    white-space: nowrap;
    box-shadow: -3px 0 0 var(--crimson-dark);
  }
</style>
</head>
<body>
  <section class="cover-banner">
    <svg class="banner-shapes" viewBox="0 0 1079 231" preserveAspectRatio="none" aria-hidden="false">
      <defs>
        <linearGradient id="crimsonFill" x1="0" y1="0" x2="1" y2="0.3">
          <stop offset="0" stop-color="var(--crimson-light)"/>
          <stop offset="0.55" stop-color="#95001a"/>
          <stop offset="1" stop-color="var(--crimson-dark)"/>
        </linearGradient>
        <linearGradient id="photoFill" x1="0" y1="0" x2="0" y2="1">
          <stop offset="0" stop-color="var(--photo-sky)"/>
          <stop offset="0.45" stop-color="var(--photo-trees)"/>
          <stop offset="1" stop-color="var(--photo-grass)"/>
        </linearGradient>
      </defs>
      <rect class="crimson-field" width="1079" height="231" fill="url(#crimsonFill)"/>
      <path class="orange-swoosh" d="M385 0 C470 40 540 190 760 231 L1079 231 L1079 0 Z" fill="var(--orange)"/>
      <path class="photo-frame" d="M500 0 C540 110 650 222 800 229 C900 233 1000 192 1079 140 L1079 0 Z" fill="var(--white)"/>
      <path class="photo-area" role="img" aria-label="Photo of the consultants sitting on grass under oak trees with their two dogs"
            d="M508 0 C548 106 656 214 800 221 C898 225 996 185 1079 133 L1079 0 Z" fill="url(#photoFill)"/>
    </svg>
    <h1 class="brand-name">
      <span class="brand-line-top">Dunmore HR</span>
      <span class="brand-line-main">Consulting</span>
    </h1>
    <p class="email-pill" style="margin:0">DunmoreHRConsulting@brelvamail.com.</p>
  </section>
</body>
</html>
```